prestige web design for KELVA Finance

Hi Guys,

Looking to team up with a creative designer for another of our websites for KELVA finance.
if looking for our similar website www.brimlendco.com.au is one of our other companies. ideally working in our logo being black and white.

Please see attachments for our logo and a description
HOME
VEHICLE
EQUIPMENT
WHO WE ARE
CONTACT US

open to ideas on layout .

touch base if you have any questions.

Target Market(s)

Prestige cars and equipment -trucks earthmoving

Industry/Entity Type

finance

Coding

Coded - Design and coding required

Number of Pages Required

5+ page

Font styles to use
Sans Serif

Colors

Designer to choose colors to be used in the design.

```html
<!DOCTYPE html>
<html lang="en">
<head>
<meta charset="utf-8">
<title>KELVA Finance – Makers of Possible</title>
<link href="https://fonts.googleapis.com/css2?family=Archivo:ital,wght@0,400;0,500;0,700;0,800;0,900;1,800;1,900&display=swap" rel="stylesheet">
<style>
  :root {
    --ink: #0b0b0b;
    --night: #0d0d0d;
    --white: #ffffff;
    --mist: #f4f4f4;
    --text: #2b2b2b;
    --muted: #4a4a4a;
    --line: #cfcfcf;
    --rock-dark: #151515;
    --rock-mid: #4a4a4a;
  }
  * { box-sizing: border-box; margin: 0; padding: 0; }
  html, body { width: 1200px; height: 3495px; overflow: hidden; }
  body { position: relative; background: var(--night); font-family: "Archivo", sans-serif; color: var(--text); }
  .abs { position: absolute; }

  /* header */
  .brand { position: absolute; display: flex; align-items: center; gap: 12px; color: var(--white);
    font-weight: 800; font-size: 40px; letter-spacing: -0.5px; }
  .brand-dot { width: 14px; height: 14px; border-radius: 50%; background: var(--white); }
  .nav { position: absolute; top: 26px; right: 60px; display: flex; align-items: center; gap: 54px; }
  .nav a { color: var(--white); text-decoration: none; font-size: 12px; font-weight: 700; letter-spacing: 1px; }
  .nav a.current { border-bottom: 2px solid var(--white); padding-bottom: 3px; }
  .nav .nav-cta { background: var(--white); color: var(--ink); padding: 11px 28px; border-radius: 22px; }

  /* hero */
  .hero { left: 0; top: 0; width: 1200px; height: 675px;
    background: linear-gradient(180deg, var(--rock-mid) 0%, #2e2e2e 35%, var(--rock-dark) 75%, #1b1b1b 100%); }
  .hero-title { left: 57px; top: 260px; color: var(--white); font-size: 90px; font-weight: 800; line-height: 108px; letter-spacing: -1px; }
  .hero-title span { border-bottom: 5px solid #9a9a9a; }
  .hero-visual { left: 600px; top: 217px; width: 540px; height: 316px; border-radius: 44px;
    background: linear-gradient(90deg, #2a9de0 0%, #2d3a6e 25%, #b9b9bd 50%, #6b2a6e 75%, #e21fb5 100%); }
  .hero-chevron { left: 579px; top: 608px; }

  /* intro */
  .intro { left: 0; top: 675px; width: 1200px; height: 412px; background: var(--night); overflow: hidden; text-align: center; color: var(--white); }
  .intro-brand { margin-top: 68px; display: inline-block; font-size: 40px; font-weight: 800; border-bottom: 2px solid var(--white); line-height: 48px; }
  .intro-copy { width: 830px; margin: 22px auto 0; font-size: 18.5px; line-height: 29px; }
  .intro-tag { position: absolute; left: 0; width: 100%; top: 376px; font-size: 40px; font-weight: 800; }

  /* why */
  .section-title { font-size: 40px; font-weight: 900; font-style: italic; color: var(--ink); letter-spacing: -0.5px; display: inline-block; border-bottom: 2px solid var(--ink); line-height: 46px; }
  .why-head { left: 0; top: 1152px; width: 1200px; text-align: center; }
  .why-sub { width: 740px; margin: 16px auto 0; font-size: 18.5px; line-height: 29px; color: var(--text); }
  .card { top: 1293px; width: 525px; height: 496px; background: var(--white); box-shadow: 0 2px 10px rgba(0,0,0,.08); text-align: center; }
  .card-photo { width: 525px; height: 302px; clip-path: polygon(0 0, 100% 0, 100% 100%, 0 95%); }
  .card-title { margin-top: 26px; font-size: 24px; font-weight: 900; font-style: italic; color: var(--ink); }
  .card-copy { width: 470px; margin: 12px auto 0; font-size: 15px; line-height: 24px; color: var(--muted); }
  .pill { display: inline-block; background: var(--ink); color: var(--white); font-size: 12px; font-weight: 700; letter-spacing: 1px; border-radius: 20px; text-decoration: none; text-align: center; }
  .card .pill { margin-top: 20px; width: 120px; height: 36px; line-height: 36px; }

  /* who */
  .who-band { left: 0; top: 1934px; width: 1200px; height: 680px; background: var(--mist); }
  .who-photo { left: 60px; top: 1863px; width: 525px; height: 601px; background: linear-gradient(135deg, #b79a7c 0%, #d8cbbd 45%, #8a5a45 75%, #c3b6a6 100%); }
  .who-text { left: 636px; top: 1997px; width: 490px; }
  .who-text p { font-size: 14.5px; line-height: 24px; color: var(--muted); margin-top: 8px; }
  .who-text .section-title { margin-bottom: 14px; }
  .who-text .pill { margin-top: 28px; width: 120px; height: 37px; line-height: 37px; }

  /* contact */
  .contact { left: 60px; top: 2538px; width: 1140px; height: 747px; background: var(--white); padding: 68px 0 0 74px; }
  .contact-lead { margin-top: 22px; font-size: 15px; color: var(--muted); }
  .call-row { margin-top: 18px; display: flex; align-items: center; font-size: 15px; color: var(--muted); }
  .call-icon { width: 38px; height: 38px; border-radius: 50%; background: var(--ink); display: flex; align-items: center; justify-content: center; margin: 0 14px; }
  .call-number { font-weight: 700; color: var(--ink); margin-right: 16px; }
  .form { margin-top: 26px; width: 691px; }
  .form-row { display: flex; gap: 15px; margin-bottom: 15px; }
  .field { flex: 1; height: 41px; border: 1px solid var(--line); font-family: inherit; font-size: 12px; color: var(--muted); padding: 0 18px; background: var(--white); }
  .field.message { height: 105px; padding-top: 14px; resize: none; }
  .form .pill { border: none; width: 106px; height: 36px; font-family: inherit; margin-top: 1px; }

  /* footer */
  .footer-links { left: 394px; top: 3360px; display: flex; gap: 32px; }
  .footer-links a { color: var(--white); text-decoration: none; font-size: 12.5px; font-weight: 700; }
  .social { left: 1010px; top: 3352px; display: flex; gap: 5px; }
  .social span { width: 33px; height: 33px; border-radius: 50%; border: 1.5px solid var(--white); }
  .social span:first-child { background: var(--white); }
  .footer-rule { left: 60px; top: 3451px; width: 1080px; height: 1px; background: #2f2f2f; }
  .copyright { left: 0; top: 3464px; width: 1200px; text-align: center; color: var(--white); font-size: 12px; font-weight: 700; letter-spacing: .5px; }
</style>
</head>
<body>

<header>
  <div class="abs hero" role="img" aria-label="Black and white photograph of a rugged mountain range"></div>
  <div class="brand" style="left:60px; top:16px;"><span class="brand-dot"></span>KELVA Finance</div>
  <nav class="nav">
    <a class="current" href="#">HOME</a>
    <a href="#">VEHICLE</a>
    <a href="#">EQUIPMENT</a>
    <a href="#">WHO WE ARE</a>
    <a class="nav-cta" href="#">CONTACT US</a>
  </nav>
  <h1 class="abs hero-title">Makers of<br><span>Possible.</span></h1>
  <div class="abs hero-visual" role="img" aria-label="Silver prestige coupe front view between blue and pink neon light bars"></div>
  <svg class="abs hero-chevron" width="42" height="24" viewBox="0 0 42 24"><polyline points="2,3 21,20 40,3" fill="none" stroke="#fff" stroke-width="2"/></svg>
</header>

<section class="abs intro">
  <h2 class="intro-brand">KELVA Finance</h2>
  <p class="intro-copy">KELVA Finance has nearly 20 years industry experience, so we certainly understand personal and business lending. We are committed to providing individuals and businesses with tailored financial services that enable them to reach and then exceed their financial goals.&nbsp; We have a vast list of lenders to suit along with an online team ready to help you, so we’re easily accessible and here when you need us. Our friendly team of experienced and approachable staff that will listen, understand your situation and lend responsibly.</p>
  <p class="intro-tag">KELVA Finance - Makers of Possible.</p>
</section>

<section>
  <div class="abs" style="left:0; top:1087px; width:1200px; height:847px; background:var(--white);"></div>
  <div class="abs why-head">
    <h2 class="section-title">WHY CHOOSE US?</h2>
    <p class="why-sub">Well, because we’re here to help you! We care about outcomes AND helping you achieve a stress and enjoyable lending experience.</p>
  </div>
  <article class="abs card" style="left:60px;">
    <div class="card-photo" role="img" aria-label="Smiling woman handing over car keys beside a dark blue car" style="background:linear-gradient(120deg,#1f2a6b 0%,#3a4796 35%,#c9ced8 60%,#8a8f99 100%);"></div>
    <h3 class="card-title">Vehicle Loan</h3>
    <p class="card-copy">While you focus on getting the right car, we will focus on getting you the right finance.</p>
    <a class="pill" href="#">APPLY NOW</a>
  </article>
  <article class="abs card" style="left:615px;">
    <div class="card-photo" role="img" aria-label="Glass jar of coins beside coin stacks with a small green plant" style="background:linear-gradient(135deg,#6e6e6e 0%,#9a9a98 40%,#a5884a 75%,#5a4a30 100%);"></div>
    <h3 class="card-title">Equipment</h3>
    <p class="card-copy">At KELVA, we help businesses of all sizes to secure funding in the form of a business loan for asset purchases from either a bank or private lender.</p>
    <a class="pill" href="#">APPLY NOW</a>
  </article>
</section>

<section>
  <div class="abs who-band"></div>
  <div class="abs who-photo" role="img" aria-label="Young couple meeting with a finance adviser at a desk"></div>
  <div class="abs who-text">
    <h2 class="section-title">WHO WE ARE</h2>
    <p>The goal of KELVA Finance is to build on the track record of the KELVA business and to create a new benchmark in the Australia’s Asset Finance industry, providing good old fashioned localised service that delivers the assets you want when you need them and structured to recognise asset useful life while being sensitive to cashflow.</p>
    <p>providing second to none asset finance support to business owners and individuals alike.</p>
    <p>A healthy appetite exists to help our customers with finance for a broad range of motor vehicles (from cars to heavy commercial vehicles), mobile and fixed plant, and business equipment…for more detail you can contact us today.</p>
    <a class="pill" href="#">READ MORE</a>
  </div>
</section>

<section class="abs contact">
  <h2 class="section-title">CONTACT US</h2>
  <p class="contact-lead">To find out how to get KELVA Finance working for you helping with your funding needs.</p>
  <div class="call-row">
    Please Call
    <span class="call-icon"><svg width="16" height="16" viewBox="0 0 24 24"><path fill="#fff" d="M6.6 10.8a15.2 15.2 0 0 0 6.6 6.6l2.2-2.2c.3-.3.7-.4 1-.2 1.1.4 2.3.6 3.6.6.6 0 1 .4 1 1V20c0 .6-.4 1-1 1A17 17 0 0 1 3 4c0-.6.4-1 1-1h3.5c.6 0 1 .4 1 1 0 1.3.2 2.5.6 3.6.1.3 0 .7-.2 1z"/></svg></span>
    <span class="call-number">13 48 27&nbsp; ( 13 KELVA)</span>
    Or Contact us now: Alternatively send us a message with your questions.
  </div>
  <form class="form">
    <div class="form-row"><input class="field" placeholder="First Name*"><input class="field" placeholder="Last Name*"></div>
    <div class="form-row"><input class="field" placeholder="Email Address*"></div>
    <div class="form-row"><input class="field" placeholder="Phone Number*"></div>
    <div class="form-row"><input class="field" placeholder="Reginal Location*"></div>
    <div class="form-row"><input class="field" placeholder="Subject*"></div>
    <div class="form-row"><textarea class="field message" placeholder="Message*"></textarea></div>
    <button class="pill" type="button">SUBMIT</button>
  </form>
</section>

<footer>
  <div class="brand" style="left:60px; top:3344px;"><span class="brand-dot"></span>KELVA Finance</div>
  <nav class="abs footer-links">
    <a href="#">Home</a><a href="#">Vehicle</a><a href="#">Equipment</a><a href="#">Who We Are</a><a href="#">Contact Us</a>
  </nav>
  <div class="abs social" aria-label="Social links"><span></span><span></span><span></span><span></span></div>
  <div class="abs footer-rule"></div>
  <p class="abs copyright">© KELVA Finance - 2022. All Rights Reserved.</p>
</footer>

</body>
</html>
```